Fernvale Craft Works business card design- Fine Art sculpture business (Contract guaranteed)

This business card is for a fine art business. Though we don't have a website up and running yet it should be up soon. I would like the business card to be elegant and fairly simple with a picture of one of my sculptures on the front (you might need to photoshop out the background) as well as my basic contact info (my name,phone # and e-mail). On the back I'd like it to be pretty simple with just "Notes" and some blank lines for writing in info.

Target Market(s)

High end artwork buyers

Industry/Entity Type

Art Gallery

Contact Information for Business Card

Marlo Prewitt Phone: (555) 213-4098 E-mail: marlo@quillbrookmail.com Facebook: @fernvalecraftworks Instagram: fernvalecraftworks

Colors

Designer to choose colors to be used in the design.

Requirements
Must have
• *A picture of one of my sculptures*, my name, business name (Fernvale Craft Works), e-mail, phone #, and a notes section on the back.
• Fernvale Craft Works
• Marlo Prewitt
• (555)213-4098
• marlo@quillbrookmail.com
• Facebook: @fernvalecraftworks
• Instagram: fernvalecraftworks
Nice to have
• It'd be nice if you can crop out the background in the sculpture pictures, which ever one you end up using.

```html
<!DOCTYPE html>
<html lang="en">
<head>
<meta charset="utf-8">
<title>Fernvale Craft Works – Business Card</title>
<link rel="stylesheet" href="https://fonts.googleapis.com/css2?family=Roboto:wght@400;500&family=Roboto+Condensed:wght@500&display=swap">
<style>
  :root {
    --page-bg: #e8e5e1;
    --card-front: #030303;
    --card-front-glow: #16201a;
    --card-back-light: #f3f3f3;
    --card-back-shade: #dcdcdc;
    --accent-purple: #7b35d1;
    --text-light: #f2f2f2;
    --rule-grey: #6a6a6a;
    --sculpture-deep: #3d1f6b;
    --sculpture-mid: #7b52b8;
    --sculpture-base: #8d8d90;
  }
  * { box-sizing: border-box; margin: 0; padding: 0; }
  html, body {
    width: 1200px; height: 960px; overflow: hidden;
    background: var(--page-bg);
    font-family: "Roboto", Arial, sans-serif;
  }
  .canvas { position: relative; width: 1200px; height: 960px; }

  .card { position: absolute; width: 601px; height: 342px; overflow: hidden;
          box-shadow: 0 3px 6px rgba(0,0,0,.35); }

  /* Front */
  .card-front { left: 302px; top: 124px; background: var(--card-front); }
  .front-backdrop {
    position: absolute; inset: 0;
    background:
      radial-gradient(ellipse 60% 70% at 65% 40%, var(--card-front-glow) 0%, transparent 75%),
      radial-gradient(ellipse 40% 50% at 90% 20%, #111a14 0%, transparent 70%),
      var(--card-front);
  }
  .sculpture-photo {
    position: absolute; left: 42px; top: 42px; width: 56px; height: 150px;
    border-radius: 22px 22px 10px 10px;
    background: linear-gradient(180deg, var(--sculpture-mid) 0%, var(--sculpture-deep) 45%, var(--sculpture-mid) 75%, var(--sculpture-base) 100%);
  }
  .brand-name {
    position: absolute; left: 112px; top: 50px;
    color: var(--accent-purple);
    font-family: "Roboto", Arial, sans-serif; font-weight: 400;
    font-size: 33px; line-height: 39px;
  }
  .contact-block { position: absolute; right: 53px; top: 206px; text-align: right; }
  .person-name {
    font-family: "Roboto Condensed", "Arial Narrow", sans-serif; font-weight: 500;
    color: var(--accent-purple); font-size: 24px; letter-spacing: .2px;
    margin-bottom: 8px;
  }
  .contact-line {
    display: flex; justify-content: flex-end; align-items: center; gap: 8px;
    color: var(--text-light); font-size: 14.5px; height: 19.5px;
  }
  .contact-icon { width: 13px; height: 13px; fill: var(--accent-purple); }

  /* Back */
  .card-back { left: 299px; top: 493px; }
  .back-backdrop {
    position: absolute; inset: 0;
    background:
      radial-gradient(ellipse 50% 45% at 30% 30%, var(--card-back-shade) 0%, transparent 70%),
      radial-gradient(ellipse 45% 40% at 75% 70%, var(--card-back-shade) 0%, transparent 70%),
      var(--card-back-light);
  }
  .notes-lines { position: absolute; left: 0; top: 0; }
</style>
</head>
<body>
<div class="canvas">

  <section class="card card-front" aria-label="Business card front">
    <div class="front-backdrop" role="img" aria-label="Dark crystal photograph background"></div>
    <div class="sculpture-photo" role="img" aria-label="Photograph of an amethyst stone sculpture on a base"></div>
    <div class="brand-name">Fernvale<br>Craft<br>Works</div>

    <div class="contact-block">
      <div class="person-name">MARLO PREWITT</div>
      <div class="contact-line">
        <span>(555) 213-4098</span>
        <svg class="contact-icon" viewBox="0 0 24 24" aria-hidden="true"><path d="M6.6 10.8c1.4 2.8 3.8 5.1 6.6 6.6l2.2-2.2c.3-.3.7-.4 1-.2 1.1.4 2.3.6 3.6.6.6 0 1 .4 1 1V20c0 .6-.4 1-1 1C10.6 21 3 13.4 3 4c0-.6.4-1 1-1h3.5c.6 0 1 .4 1 1 0 1.3.2 2.5.6 3.6.1.3 0 .7-.2 1z"/></svg>
      </div>
      <div class="contact-line">
        <span>marlo.prewitt4@quillbrookmail.com</span>
        <svg class="contact-icon" viewBox="0 0 24 24" aria-hidden="true"><path d="M2 5h20v14H2z M3.5 6.5 12 13l8.5-6.5" fill="var(--accent-purple)" stroke="var(--card-front)" stroke-width="1.4"/></svg>
      </div>
      <div class="contact-line">
        <span>www.fernvalecraftworks.com</span>
        <svg class="contact-icon" viewBox="0 0 24 24" aria-hidden="true"><circle cx="12" cy="12" r="10"/><path d="M2 12h20M12 2c3 3 3 17 0 20M12 2c-3 3-3 17 0 20" fill="none" stroke="var(--card-front)" stroke-width="1.5"/></svg>
      </div>
    </div>
  </section>

  <section class="card card-back" aria-label="Business card back, notes">
    <div class="back-backdrop" role="img" aria-label="Pale crystal photograph background"></div>
    <svg class="notes-lines" width="601" height="342" viewBox="0 0 601 342" aria-hidden="true">
      <g stroke="var(--rule-grey)" stroke-width="1.2">
        <line x1="46" y1="69" x2="555" y2="69"/>
        <line x1="46" y1="123" x2="555" y2="123"/>
        <line x1="46" y1="177" x2="555" y2="177"/>
        <line x1="46" y1="232" x2="555" y2="232"/>
        <line x1="46" y1="286" x2="555" y2="286"/>
      </g>
    </svg>
  </section>

</div>
</body>
</html>
```